3 signs to go on a trailer

due to logo change we need to update our trailer design signage the trailer has 3 panels 2 panels @ 650mmx1200 1@500mmx1200, i have attached a sample i was working on please feel free to change anything you feel needs change. im trying to achive a simple and soft design. i also uploaded our new logo in AI file, please feel free to contact me for further information. also a sketch of how the trailer looks like

```html
<!DOCTYPE html>
<html lang="en">
<head>
<meta charset="utf-8">
<title>Brightwash trailer signage</title>
<link rel="stylesheet" href="https://fonts.googleapis.com/css2?family=Nunito:wght@700;800;900&display=swap">
<style>
  :root {
    --bg: #e4e4e4;
    --green-deep: #0d6b32;
    --green-mid: #1f9a3d;
    --green-bright: #3fae3a;
    --green-badge: #136b34;
    --green-text: #0f5a2c;
    --yellow-soft: #f3f29a;
    --yellow-pale: #fbf8c4;
    --ink: #3a3a3a;
    --red: #d52b1e;
    --white: #ffffff;
  }
  * { box-sizing: border-box; margin: 0; padding: 0; }
  html, body { width: 1200px; height: 960px; overflow: hidden; }
  body {
    background: var(--bg);
    font-family: "Nunito", sans-serif;
    position: relative;
  }
  .panel {
    position: absolute;
    top: 212px;
    height: 536px;
    overflow: hidden;
  }
  .panel--services {
    left: 102px; width: 292px;
    background: linear-gradient(160deg, var(--green-bright) 0%, var(--green-mid) 45%, var(--green-deep) 100%);
  }
  .panel--features {
    left: 496px; width: 224px;
    background: radial-gradient(ellipse at 50% 45%, var(--yellow-pale) 0%, var(--yellow-soft) 55%, #c9df6a 100%);
  }
  .panel--blasting { left: 822px; width: 290px; }
  .photo-fill {
    position: absolute; inset: 0;
    background: linear-gradient(135deg, #4fa52a 0%, #8ab834 40%, #5c9a24 70%, #2f7a1f 100%);
  }
  .badge {
    position: absolute;
    width: 152px; height: 152px;
    border-radius: 50%;
    background: var(--green-badge);
  }
  .badge--services { left: 70px; top: -66px; }
  .badge--blasting { left: 68px; top: -64px; }
  .badge-text {
    position: absolute; left: 0; right: 0;
    text-align: center;
    color: var(--white);
    font-weight: 800;
    letter-spacing: 0.5px;
  }
  .badge-text--services { top: 15px; font-size: 17px; line-height: 20px; }
  .badge-text--blasting { top: 12px; font-size: 16px; line-height: 19px; }
  .badge-text__code {
    display: inline-block;
    font-size: 13px; line-height: 16px;
    margin-top: 3px; padding: 2px 8px 0;
    border-top: 1px solid rgba(255,255,255,0.7);
    letter-spacing: 1px;
  }
  .service-list {
    position: absolute; left: 0; right: 0; top: 92px;
    text-align: center;
    color: var(--green-text);
    font-weight: 800; font-size: 16px; line-height: 20px;
    letter-spacing: 0.5px;
  }
  .brand-dot {
    position: absolute;
    width: 150px; height: 150px;
    border-radius: 50%;
    background: var(--white);
  }
  .panel--services .brand-dot, .panel--blasting .brand-dot { left: 70px; top: 326px; }
  .brand-name {
    position: absolute; left: 0; right: 0;
    text-align: center;
    font-weight: 900;
    font-size: 30px; line-height: 36px;
    letter-spacing: 0.5px;
    color: var(--white);
  }
  .panel--services .brand-name, .panel--blasting .brand-name { top: 480px; }
  .feature {
    position: absolute; top: 0;
    width: 28px;
    background: var(--green-badge);
    border-radius: 0 0 14px 14px;
    display: flex; align-items: flex-end; justify-content: center;
    padding-bottom: 10px;
  }
  .feature--pressure { left: 14px; height: 220px; }
  .feature--heat { left: 70px; height: 206px; background: #1d8a3a; }
  .feature--chem { left: 125px; height: 182px; background: #2fa53c; }
  .feature--eco { left: 179px; height: 230px; }
  .feature__text {
    writing-mode: vertical-rl;
    transform: rotate(180deg);
    color: var(--white);
    font-weight: 800; font-size: 14px;
    letter-spacing: 1px;
    white-space: nowrap;
  }
  .panel--features .brand-dot {
    left: 26px; top: 263px; width: 166px; height: 166px;
    background: var(--green-mid);
  }
  .panel--features .brand-name { top: 432px; color: var(--ink); font-size: 27px; line-height: 34px; }
  .contact-phone {
    position: absolute; left: 0; right: 0; top: 466px;
    text-align: center; color: var(--red);
    font-weight: 800; font-size: 25px; line-height: 32px;
  }
  .contact-web {
    position: absolute; left: 0; right: 0; top: 499px;
    text-align: center; color: var(--ink);
    font-weight: 800; font-size: 13.5px; line-height: 18px; letter-spacing: 1px;
  }
</style>
</head>
<body>
  <section class="panel panel--services">
    <div class="badge badge--services"></div>
    <p class="badge-text badge-text--services">Integrated<br>Services</p>
    <p class="service-list">Cleaning<br>Security<br>Maintenance</p>
    <div class="brand-dot"></div>
    <div class="brand-name">BRIGHTWASH</div>
  </section>

  <section class="panel panel--features">
    <div class="feature feature--pressure"><span class="feature__text">5800PSI PRESSURE</span></div>
    <div class="feature feature--heat"><span class="feature__text">150°C HOT WATER</span></div>
    <div class="feature feature--chem"><span class="feature__text">NO CHEMICALS</span></div>
    <div class="feature feature--eco"><span class="feature__text">100% ECO FRIENDLY</span></div>
    <div class="brand-dot"></div>
    <div class="brand-name">BRIGHTWASH</div>
    <div class="contact-phone">1300 555 019</div>
    <div class="contact-web">www.brightwash.com.au</div>
  </section>

  <section class="panel panel--blasting">
    <div class="photo-fill" role="img" aria-label="Photo of a pressure washer nozzle spraying a jet of water across green-tinted timber decking"></div>
    <div class="badge badge--blasting"></div>
    <p class="badge-text badge-text--blasting">Water Blasting<br>Division<br><span class="badge-text__code">TN003</span></p>
    <div class="brand-dot"></div>
    <div class="brand-name">BRIGHTWASH</div>
  </section>
</body>
</html>
```